advertising board Hovarlunde BV

I have an advertisement spot in a small indoor football stadium, with the size of 1.00 x 22.00 meters. I want to show a design that stands out. My company works in Civil constructions and actually installs steel sheet piles and earth retaining walls in the most difficult to reach locations.

```html
<!DOCTYPE html>
<html lang="en">
<head>
<meta charset="utf-8">
<title>Hovarlunde BV – Stadium Advertising Board</title>
<link href="https://fonts.googleapis.com/css2?family=Oswald:wght@300;400;600;700&display=swap" rel="stylesheet">
<style>
  :root {
    --page-bg: #b3b3b3;
    --board-white: #ffffff;
    --brand-blue: #1592dc;
    --brand-blue-dark: #0a6fb8;
    --brand-blue-light: #3aa9ea;
    --band-dark: #3a3a3c;
    --logo-ink: #2b2b2b;
    --text-white: #ffffff;
  }
  * { margin: 0; padding: 0; box-sizing: border-box; }
  html, body {
    width: 1200px; height: 1200px; overflow: hidden;
    background: var(--page-bg);
    font-family: "Oswald", "Arial Narrow", sans-serif;
  }
  .board {
    position: absolute; left: 515px; top: 110px;
    width: 170px; height: 985px;
    background: var(--board-white);
    overflow: hidden;
  }
  .board > * { position: absolute; left: 0; width: 100%; }

  .brand { top: 15px; height: 35px; }
  .brand-mark {
    position: absolute; left: 0; top: 2px; width: 24px; height: 24px;
    background: var(--brand-blue);
  }
  .brand-name {
    position: absolute; left: 30px; top: 0;
    font-weight: 600; font-size: 19px; line-height: 26px;
    color: var(--logo-ink);
  }
  .brand-tagline {
    position: absolute; left: 30px; top: 25px; right: 4px;
    font-weight: 300; font-size: 4.4px; letter-spacing: .1px;
    color: var(--logo-ink); white-space: nowrap; overflow: hidden;
  }

  .panel {
    left: 10px; width: 150px;
    background: linear-gradient(180deg, var(--brand-blue-light), var(--brand-blue) 55%, var(--brand-blue-dark));
    color: var(--text-white); text-align: center;
  }
  .panel-civil { top: 78px; height: 135px; padding-top: 14px; }
  .panel-steel { top: 328px; height: 285px; padding-top: 14px; }

  .lead { font-weight: 300; font-size: 26px; line-height: 32px; }
  .lead-small { font-weight: 300; font-size: 16px; line-height: 26px; }
  .headline { font-weight: 700; font-size: 40px; line-height: 44px; text-transform: uppercase; }
  .subline { font-weight: 600; font-size: 17px; line-height: 20px; text-transform: uppercase; }

  .photo-site {
    top: 213px; height: 115px;
    background: linear-gradient(180deg, #8fc3ec 0%, #c9e0f2 50%, #8a8a86 80%, #6d5a48 100%);
  }
  .pipes {
    position: absolute; left: 0; right: 0; bottom: 0; height: 153px;
    background: linear-gradient(180deg, rgba(10,111,184,0) 0%, #0c7dc6 45%, #075f9e 100%);
  }

  .earth {
    top: 627px; height: 90px; text-align: center; color: var(--brand-blue);
  }
  .earth .lead-small { color: var(--logo-ink); font-size: 16px; line-height: 24px; }
  .earth .headline { font-size: 40px; line-height: 42px; }
  .earth .subline { font-size: 17px; }

  .band {
    top: 727px; height: 55px; background: var(--band-dark);
    color: var(--text-white); text-align: center;
    font-weight: 300; font-size: 16px; line-height: 21px; padding-top: 6px;
  }

  .photo-worker {
    top: 797px; height: 188px;
    background: linear-gradient(180deg, #9aa3ad 0%, #b9bfc6 40%, #d98b3a 62%, #8c8c88 100%);
  }
</style>
</head>
<body>
  <div class="board">
    <div class="brand">
      <span class="brand-mark"></span>
      <span class="brand-name">Hovarlunde</span>
      <span class="brand-tagline">civiele werken · damwanden · grondkeringen · funderingen</span>
    </div>

    <div class="panel panel-civil">
      <p class="lead">We works</p>
      <p class="headline">Civil</p>
      <p class="subline">Constructions</p>
    </div>

    <div class="photo-site" role="img" aria-label="Photo of a bridge construction site with cranes under a blue sky"></div>

    <div class="panel panel-steel">
      <p class="lead-small">and actually installs</p>
      <p class="headline">Steel</p>
      <p class="subline">Sheet piles</p>
      <div class="pipes" role="img" aria-label="Illustration of upright blue steel pipes of varying heights"></div>
    </div>

    <div class="earth">
      <p class="lead-small">and</p>
      <p class="headline">Earth</p>
      <p class="subline">Retaining walls</p>
    </div>

    <div class="band">
      <p>in the most difficult<br>to reach locations.</p>
    </div>

    <div class="photo-worker" role="img" aria-label="Photo of a construction engineer in a hard hat and safety vest reviewing plans on site"></div>
  </div>
</body>
</html>
```